Modern business card for triathlon training business in Australia

We need a business card design for our triathlon training company.

Pace with Us Fitness is an Australian business, owned by women, run for women. Pace with Us Fitness helps women prepare or improve triathlon skills and confidence through triathlon camps completely designed for women.

Our camps focus on preparing women both physically and mentally for their next (or first!) triathlon.

You can see our website www.pacewithusfitness.com.au for more info about our business and our style.

We've attached two of our logos and are happy to consider a design that utilised either colour scheme with the teal colour being our 'feature' colour. We don't want overly feminine cards but rather cards that are professional and neat. If the inclusion of any pictures/art is warranted, this should be focused on our swim/ride/run theme and in that specific order (swim/ride/run).

The business card needs to be a printable design and the contact details will need to change for our two employees.

Target Market(s)

Female clients and partners/vendors/sponsors that we work with in the triathlon industry

Industry/Entity Type

Fitness

Contact Information for Business Card

Pace with Us Fitness (business name)
Nina Carver
Business Director
Mobile: 0438 916 207
Email: nina@pacewithusfitness.com.au
www.pacewithusfitness.com.au

Second business card:
Pace with Us Fitness
Bel Stray
Coaching Director
Mobile: 0459 260 718
Email: bel@pacewithusfitness.com.au

Font styles to use
Serif
Sans Serif

Requirements
Must have
• Core contact details above, our logo and be a printable design
Should not have
• Pink
• Cursive/script fonts

```html
<!DOCTYPE html>
<html lang="en">
<head>
<meta charset="utf-8">
<title>Pace with Us Fitness – Business Card</title>
<link rel="stylesheet" href="https://fonts.googleapis.com/css2?family=Mulish:wght@400;600;700&display=swap">
<style>
  :root {
    --teal: #1fb3c4;
    --ink: #5a5f63;
    --ink-soft: #7c8186;
    --card: #ffffff;
    --backdrop: #eceeef;
  }
  * { margin: 0; padding: 0; box-sizing: border-box; }
  html, body {
    width: 1200px;
    height: 903px;
    overflow: hidden;
    background: var(--backdrop);
    font-family: "Mulish", Arial, sans-serif;
  }
  .canvas {
    width: 1200px;
    height: 903px;
    display: flex;
    align-items: center;
    justify-content: center;
  }
  .business-card {
    position: relative;
    width: 900px;
    height: 514px;
    background: var(--card);
    box-shadow: 0 10px 30px rgba(0,0,0,0.12);
    overflow: hidden;
  }
  .edge-band {
    position: absolute;
    left: 0; right: 0; bottom: 0;
    height: 12px;
    background: var(--teal);
  }
  .accent-bar {
    position: absolute;
    top: 0;
    left: 250px;
    width: 250px;
    height: 16px;
    background: var(--teal);
  }
  .contact {
    position: absolute;
    top: 58px;
    left: 60px;
  }
  .contact-name {
    color: var(--teal);
    font-weight: 600;
    font-size: 26px;
    letter-spacing: 0.2px;
  }
  .contact-role {
    color: var(--ink-soft);
    font-size: 18px;
    margin-top: 4px;
  }
  .icon-row {
    display: flex;
    gap: 6px;
    margin-top: 22px;
  }
  .icon-tile {
    width: 22px;
    height: 22px;
    background: var(--teal);
    border-radius: 3px;
    display: flex;
    align-items: center;
    justify-content: center;
  }
  .contact-lines {
    list-style: none;
    margin-top: 10px;
    color: var(--ink);
    font-size: 18px;
    line-height: 1.55;
  }
  .brand {
    position: absolute;
    right: 70px;
    top: 320px;
    display: flex;
    align-items: center;
    gap: 12px;
  }
  .brand-dot {
    width: 18px;
    height: 18px;
    border-radius: 50%;
    background: var(--teal);
  }
  .brand-name {
    color: var(--teal);
    font-weight: 700;
    font-size: 32px;
    text-transform: uppercase;
    letter-spacing: 1px;
    white-space: nowrap;
  }
</style>
</head>
<body>
<main class="canvas">
  <article class="business-card">
    <div class="accent-bar"></div>

    <section class="contact">
      <h1 class="contact-name">Nina Carver</h1>
      <p class="contact-role">Business Director</p>
      <div class="icon-row">
        <span class="icon-tile">
          <svg width="14" height="14" viewBox="0 0 14 14" aria-label="phone">
            <rect x="4" y="1" width="6" height="12" rx="1.2" fill="none" stroke="#fff" stroke-width="1.4"/>
            <circle cx="7" cy="10.8" r="0.8" fill="#fff"/>
          </svg>
        </span>
        <span class="icon-tile">
          <svg width="14" height="14" viewBox="0 0 14 14" aria-label="email">
            <rect x="1.5" y="3" width="11" height="8" fill="none" stroke="#fff" stroke-width="1.4"/>
            <path d="M1.5 3 L7 8 L12.5 3" fill="none" stroke="#fff" stroke-width="1.4"/>
          </svg>
        </span>
        <span class="icon-tile">
          <svg width="14" height="14" viewBox="0 0 14 14" aria-label="website">
            <circle cx="7" cy="7" r="5.5" fill="none" stroke="#fff" stroke-width="1.3"/>
            <ellipse cx="7" cy="7" rx="2.3" ry="5.5" fill="none" stroke="#fff" stroke-width="1.1"/>
            <line x1="1.5" y1="7" x2="12.5" y2="7" stroke="#fff" stroke-width="1.1"/>
          </svg>
        </span>
      </div>
      <ul class="contact-lines">
        <li>0438 916 207</li>
        <li>nina@pacewithusfitness.com.au</li>
        <li>www.pacewithusfitness.com.au</li>
      </ul>
    </section>

    <div class="brand">
      <span class="brand-dot"></span>
      <span class="brand-name">Pace with Us Fitness</span>
    </div>

    <div class="edge-band"></div>
  </article>
</main>
</body>
</html>
```